Valdor Real Estate Agency Business Card Design

Hello again, I'd like for you to design our new business cards and letterhead if you can. The cards will be printed on a white/off-white thick card stock. I wanted the color version of the logo alone on one side (possibly with our website URL and maybe the words Residential & Commercial Sales & Leasing), and the below info (listed in business card details) for the other side (or you choose whatever sides look best because I trust your judgement).

Target Market(s)

Property owners, property management companies, buyers & sellers of real estate property

Industry/Entity Type

Real Estate

Contact Information for Business Card

Personal Info:
Peter Loweny
Licensed Real Estate Broker
Mobile: (212) 555-0148
ploweny@valdorhomes.example

Company Info:
Valdor Agency LLC
18-22 41st Avenue, 3FL
Long Island City, NY 11109
www.valdorhomes.example
Office: (718) 555-0193

Of course the personal info should be editable so I can order cards for other agents in the future.

Let me know if you have any questions. Looking forward to seeing your ideas.

Requirements
Nice to have
• Some red elements to match the logo but not much
Should not have
• Not too busy, I would like a minimal but professional look.

```html
<!DOCTYPE html>
<html lang="en">
<head>
<meta charset="utf-8">
<title>Valdor Real Estate Agency – Business Card</title>
<link rel="stylesheet" href="https://fonts.googleapis.com/css2?family=Open+Sans:wght@400;600;700&display=swap">
<style>
  :root {
    --backdrop: #e4e2df;
    --card: #fbfbf9;
    --ink: #3a3a3a;
    --ink-soft: #555555;
    --accent: #e0231b;
    --rule: #3a3a3a;
  }
  * { box-sizing: border-box; margin: 0; padding: 0; }
  html, body {
    width: 1200px;
    height: 794px;
    overflow: hidden;
    background: var(--backdrop);
  }
  .canvas {
    position: relative;
    width: 1200px;
    height: 794px;
    display: flex;
    align-items: center;
    justify-content: center;
    gap: 50px;
  }
  .card {
    position: relative;
    width: 525px;
    height: 300px;
    background: var(--card);
    box-shadow: 0 2px 10px rgba(0,0,0,0.12);
    color: var(--ink);
    font-family: "Open Sans", sans-serif;
  }

  /* Brand placeholder: plain name set in the card's text font */
  .brand {
    display: flex;
    flex-direction: column;
  }
  .brand-name {
    font-family: "Open Sans", sans-serif;
    font-weight: 700;
    color: var(--ink);
    line-height: 1;
    letter-spacing: 0.02em;
  }
  .brand-tagline {
    font-family: "Open Sans", sans-serif;
    font-weight: 400;
    color: var(--ink-soft);
    text-transform: uppercase;
    white-space: nowrap;
  }

  /* Front side */
  .card-front {
    display: flex;
    align-items: center;
    justify-content: center;
  }
  .card-front .brand-name { font-size: 84px; }
  .card-front .brand-tagline {
    font-size: 11.5px;
    letter-spacing: 0.2em;
    margin-top: 12px;
    margin-left: 4px;
  }

  /* Back side */
  .card-back { padding: 26px 30px 24px; }
  .card-back .brand-name { font-size: 56px; }
  .card-back .brand-tagline {
    font-size: 8.6px;
    letter-spacing: 0.2em;
    margin-top: 8px;
    margin-left: 3px;
  }
  .agent {
    position: absolute;
    right: 30px;
    top: 128px;
    text-align: right;
  }
  .agent-name {
    font-size: 15px;
    font-weight: 700;
    text-transform: uppercase;
    color: var(--ink);
    letter-spacing: 0.01em;
  }
  .agent-title {
    font-size: 11px;
    font-weight: 700;
    color: var(--accent);
  }
  .divider {
    position: absolute;
    left: 30px;
    right: 30px;
    top: 172px;
    height: 1.5px;
    background: var(--rule);
  }
  .details {
    position: absolute;
    left: 30px;
    right: 30px;
    top: 186px;
    display: flex;
    gap: 44px;
    font-weight: 700;
    font-size: 11.5px;
    color: var(--ink);
    line-height: 1.55;
  }
  .contact-list { list-style: none; }
  .contact-list li {
    display: flex;
    align-items: center;
    gap: 8px;
  }
  .contact-icon {
    width: 12px;
    height: 12px;
    flex: none;
  }
  .office-address { font-style: normal; }
</style>
</head>
<body>
<main class="canvas">

  <section class="card card-front" aria-label="Business card, brand side">
    <div class="brand">
      <div class="brand-name">Valdor</div>
      <div class="brand-tagline">Residential &amp; Commercial Sales &amp; Leasing</div>
    </div>
  </section>

  <section class="card card-back" aria-label="Business card, contact side">
    <div class="brand">
      <div class="brand-name">Valdor</div>
      <div class="brand-tagline">Residential &amp; Commercial Sales &amp; Leasing</div>
    </div>

    <div class="agent">
      <div class="agent-name">Peter Loweny</div>
      <div class="agent-title">Real Estate Broker</div>
    </div>

    <div class="divider"></div>

    <div class="details">
      <ul class="contact-list">
        <li>
          <svg class="contact-icon" viewBox="0 0 12 12" aria-hidden="true">
            <rect x="2.5" y="0.5" width="7" height="11" rx="1.2" fill="none" stroke="var(--accent)" stroke-width="1.3"/>
            <rect x="4.5" y="9" width="3" height="1" fill="var(--accent)"/>
          </svg>
          (212) 555-0148
        </li>
        <li>
          <svg class="contact-icon" viewBox="0 0 12 12" aria-hidden="true">
            <rect width="12" height="12" rx="1.5" fill="var(--accent)"/>
            <path d="M3 4.2c0-.8.7-1.2 3-1.2s3 .4 3 1.2v.8H7.6v-.7H4.4v.7H3z M3.6 6h4.8l.6 3H3z" fill="#fff"/>
          </svg>
          (718) 555-0193
        </li>
        <li>
          <svg class="contact-icon" viewBox="0 0 12 12" aria-hidden="true">
            <rect width="12" height="12" rx="1.5" fill="var(--accent)"/>
            <path d="M2.2 3.5h7.6v5H2.2z M2.2 3.5 6 6.5l3.8-3" fill="none" stroke="#fff" stroke-width="0.9"/>
          </svg>
          ploweny@valdorhomes.example
        </li>
        <li>
          <svg class="contact-icon" viewBox="0 0 12 12" aria-hidden="true">
            <circle cx="6" cy="6" r="6" fill="var(--accent)"/>
            <g fill="none" stroke="#fff" stroke-width="0.8">
              <circle cx="6" cy="6" r="4"/>
              <ellipse cx="6" cy="6" rx="1.8" ry="4"/>
              <path d="M2 6h8"/>
            </g>
          </svg>
          www.valdorhomes.example
        </li>
      </ul>

      <address class="office-address">
        Valdor Agency LLC<br>
        18-22 41st Avenue,<br>
        3FL Long Island City,<br>
        NY 11109
      </address>
    </div>
  </section>

</main>
</body>
</html>
```